Endocrinologist needs new stationery

I have a logo from MarkForge and now need stationery with the new logo.

Address: Suite 4, 282 Falcon Street, Richmond, VIC 3121
Phone: 03 9417 2253
Fax: 03 9417 2255
Website: www.drmaylacorwen.com.au
Email: admin@drmaylacorwen.com.au

```html
<!DOCTYPE html>
<html lang="en">
<head>
<meta charset="utf-8">
<title>Dr Mayla Corwen – Stationery Suite</title>
<link href="https://fonts.googleapis.com/css2?family=Montserrat:wght@500&family=Open+Sans:wght@400&family=Tinos&display=swap" rel="stylesheet">
<style>
:root{
  --bg:#e8e8e8;
  --paper:#ffffff;
  --mauve:#7a5a6e;
  --blue:#3e72a4;
  --heading:#3d6e9e;
  --ink:#333333;
}
*{margin:0;padding:0;box-sizing:border-box}
html,body{width:1200px;height:658px;overflow:hidden;background:var(--bg)}
.canvas{position:relative;width:1200px;height:658px}
.section-title{position:absolute;font-family:"Montserrat",sans-serif;font-weight:500;font-size:15px;letter-spacing:2.6px;color:var(--heading);transform:translateX(-50%);white-space:nowrap}
.sheet{position:absolute;background:var(--paper);overflow:hidden;box-shadow:0 2px 6px rgba(0,0,0,.18)}
.wave{position:absolute;left:0;bottom:0;width:100%}
.brand{position:absolute;font-family:"Tinos",serif;color:var(--blue);white-space:nowrap;line-height:1}
.contact{font-family:"Tinos",serif;color:var(--blue);white-space:nowrap;line-height:1.3}
.icon{display:inline-block;width:.85em;height:.85em;border-radius:50%;background:var(--mauve);vertical-align:-1px;margin-right:1px}

/* business cards */
.card{left:102px;width:226px;height:129px}
.card--front{top:101px}
.card--back{top:245px}
.card--front .brand{left:0;right:0;top:45px;text-align:center;font-size:24px}
.card--back .brand{left:0;right:0;top:20px;text-align:center;font-size:13px}
.card-contacts{position:absolute;top:71px;font-size:6.6px}
.card-contacts--left{left:26px}
.card-contacts--right{left:112px}
.indent{padding-left:8px}

/* compliment slip */
.slip{left:68px;top:435px;width:293px;height:121px}
.slip .brand{left:12px;top:14px;font-size:14px}
.slip-script{position:absolute;right:10px;top:12px;width:78px;height:22px;background:linear-gradient(90deg,#ece3e8,#e2d6dd);border-radius:3px}
.slip-contacts{position:absolute;left:0;right:0;top:92px;text-align:center;font-size:5.2px}

/* letterhead */
.letter{left:402px;top:95px;width:324px;height:450px}
.letter .brand{left:0;right:0;top:31px;text-align:center;font-size:28px}
.letter-body{position:absolute;left:35px;right:35px;font-family:"Open Sans",sans-serif;font-size:5.2px;line-height:8.8px;color:var(--ink)}
.letter-date{position:absolute;right:35px;top:89px;font-family:"Open Sans",sans-serif;font-size:5.2px;color:var(--ink)}
.recipient{top:114px}
.salutation{top:164px}
.paragraphs{top:181px}
.paragraphs p{margin-bottom:8.8px}
.signoff{top:348px}
.letter-contacts{position:absolute;left:0;right:0;top:401px;text-align:center;font-size:6.2px}
.letter-contacts span{margin:0 5px}

/* envelopes */
.dl{left:769px;top:98px;width:379px;height:175px}
.dl .brand{left:0;right:0;top:22px;text-align:center;font-size:18px;color:var(--paper)}
.flap{position:absolute;left:0;top:0;width:100%;height:92px}
.window-env{left:769px;top:345px;width:379px;height:175px}
.window-env .brand{left:17px;top:15px;font-size:17px}
.return-address{position:absolute;left:17px;top:51px;font-size:5.8px}
.address-window{position:absolute;left:201px;top:75px;width:138px;height:50px;border-radius:6px;background:#e3e3e3;box-shadow:0 1px 3px rgba(0,0,0,.25)}
</style>
</head>
<body>
<div class="canvas">

  <svg width="0" height="0" style="position:absolute" aria-hidden="true">
    <defs>
      <g id="wave-right">
        <path d="M0,0 C250,70 520,110 1000,0 L1000,100 L0,100Z" fill="#7a5a6e"/>
        <path d="M430,100 C600,55 820,40 1000,38 L1000,100Z" fill="#3e72a4"/>
        <path d="M450,92 C600,70 700,62 760,58 C680,70 560,85 470,96Z" fill="#ffffff"/>
      </g>
    </defs>
  </svg>

  <div class="section-title" style="left:215px;top:75px">BUSINESS CARD</div>
  <div class="section-title" style="left:564px;top:64px">LETTER HEAD</div>
  <div class="section-title" style="left:959px;top:64px">DL ENVELOPES</div>
  <div class="section-title" style="left:959px;top:310px">WINDOW ENVELOPES</div>
  <div class="section-title" style="left:215px;top:410px">COMPLIMENT SLIP</div>

  <!-- Business card front -->
  <div class="sheet card card--front">
    <div class="brand">Dr Mayla Corwen</div>
    <svg class="wave" style="height:28px" viewBox="0 0 1000 100" preserveAspectRatio="none"><use href="#wave-right"/></svg>
  </div>

  <!-- Business card back -->
  <div class="sheet card card--back">
    <div class="brand">Dr Mayla Corwen</div>
    <div class="contact card-contacts card-contacts--left">
      <div><i class="icon"></i>03 9417 2253</div>
      <div><i class="icon"></i>Suite 4, 282 Falcon Street,</div>
      <div class="indent">Richmond, VIC 3121</div>
    </div>
    <div class="contact card-contacts card-contacts--right">
      <div><i class="icon"></i>03 9417 2255</div>
      <div><i class="icon"></i>www.drmaylacorwen.com.au</div>
      <div><i class="icon"></i>admin@drmaylacorwen.com.au</div>
    </div>
    <svg class="wave" style="height:28px;transform:scaleX(-1)" viewBox="0 0 1000 100" preserveAspectRatio="none"><use href="#wave-right"/></svg>
  </div>

  <!-- Compliment slip -->
  <div class="sheet slip">
    <div class="brand">Dr Mayla Corwen</div>
    <div class="slip-script" role="img" aria-label="Handwritten 'With Compliments' lettering"></div>
    <div class="contact slip-contacts">
      <div><i class="icon"></i>03 9417 2253 &nbsp; <i class="icon"></i>03 9417 2255 &nbsp; <i class="icon"></i>admin@drmaylacorwen.com.au &nbsp; <i class="icon"></i>www.drmaylacorwen.com.au</div>
      <div><i class="icon"></i>Suite 4, 282 Falcon Street, Richmond, VIC 3121</div>
    </div>
    <svg class="wave" style="height:21px" viewBox="0 0 1000 100" preserveAspectRatio="none"><use href="#wave-right"/></svg>
  </div>

  <!-- Letterhead -->
  <div class="sheet letter">
    <div class="brand">Dr Mayla Corwen</div>
    <div class="letter-date">2nd May, 2025</div>
    <div class="letter-body recipient">Harriet Lindqvist<br>123 Anywhere St.,<br>Any City,<br>ST 12345</div>
    <div class="letter-body salutation">To whom it may concern,</div>
    <div class="letter-body paragraphs">
      <p>Lorem ipsum dolor sit amet, consectetur adipiscing elit. Sed malesuada urna dui, efficitur aliquam leo congue at. Aliquam eget molestie magna. Fusce gravida ante nec mi fermentum pretium. Integer sit amet mollis risus. Donec non finibus ante. Duis in tempus dui. Nam id lectus leo. Vivamus at mauris facilisis, consectetur lectus id, pharetra dui. Suspendisse porta justo augue, quis iaculis ex pellentesque sed. Curabitur vitae tincidunt nulla.</p>
      <p>Proin et varius nulla. Phasellus augue quam, placerat in elit consectetur, accumsan tempus ipsum. Curabitur gravida felis et purus aliquet, id suscipit nibh lacinia. Aliquam feugiat eros ac tellus cursus tincidunt. Ut id quam ut sem dictum aliquet. Aenean volutpat felis eros, vitae sagittis tortor commodo vitae. Duis lobortis porta ante, id mollis diam gravida quis.</p>
      <p>Cras posuere quis elit non ultricies. Maecenas malesuada nisl id nibh pellentesque, et cursus sapien semper. Duis mollis, tellus sollicitudin lobortis mollis, diam diam scelerisque felis, quis pellentesque neque dolor non ligula. Nam urna dolor, lacinia et erat sit amet, viverra porta diam. Ut mollis elementum accumsan. Morbi et tellus vitae quam sodales auctor. Maecenas pulvinar risus vel ornare rutrum. Curabitur sed fringilla sapien. Vivamus vel nisl nibh. Donec id blandit justo. Duis vitae varius dolor, eu pulvinar lacus.</p>
    </div>
    <div class="letter-body signoff">Yours sincerely,<br>Tomas Reyland</div>
    <div class="contact letter-contacts">
      <div><span><i class="icon"></i>03 9417 2253</span><span><i class="icon"></i>03 9417 2255</span><span><i class="icon"></i>admin@drmaylacorwen.com.au</span><span><i class="icon"></i>www.drmaylacorwen.com.au</span></div>
      <div style="margin-top:3px"><i class="icon"></i>Suite 4, 282 Falcon Street, Richmond, VIC 3121</div>
    </div>
    <svg class="wave" style="height:40px" viewBox="0 0 1000 100" preserveAspectRatio="none"><use href="#wave-right"/></svg>
  </div>

  <!-- DL envelope -->
  <div class="sheet dl">
    <svg class="flap" viewBox="0 0 815 200" preserveAspectRatio="none" aria-hidden="true">
      <path d="M0,0 L815,0 C795,70 785,95 755,108 L430,193 Q408,199 386,193 L70,112 C40,100 25,75 0,0Z" fill="#7a5a6e"/>
    </svg>
    <div class="brand">Dr Mayla Corwen</div>
  </div>

  <!-- Window envelope -->
  <div class="sheet window-env">
    <div class="brand">Dr Mayla Corwen</div>
    <div class="contact return-address">Suite 4, 282 Falcon Street,<br>Richmond, VIC 3121</div>
    <div class="address-window"></div>
    <svg class="wave" style="height:44px" viewBox="0 0 1000 100" preserveAspectRatio="none"><use href="#wave-right"/></svg>
  </div>

</div>
</body>
</html>
```